Lawn care business card

I am looking for a quality designed personal business card to represent the quality and elegant nature of our company. We separate ourselves in our market by the aesthetic value of our work, so I am looking for marketing material that does the same. We target our marketing high end customers, and we try to avoid price shoppers. I am open to all design options, so long as they are in line with our companies values.

We are tend to go with a retro look on everything from our logo and print material, to our uniforms. We like to portray and "old fashion" set of core values, with a modern elegance. So a wild and crazy look is out of the question.

Things I'd like on the card:
1.) Logo
2.) Phone number: (816) 555-0193
3.) Website: Verdantix.com
4.) Email: peterholloway@verdantix.com
5.) My name: Peter Holloway
6.) Facebook link: facebook.com/VerdantixGroundsandGarden
7.) Instagram: http://instagram.com/verdantix

Attached is a copy of our logo.

```html
<!DOCTYPE html>
<html lang="en">
<head>
<meta charset="utf-8">
<title>Larkmoor — Business Card</title>
<link href="https://fonts.googleapis.com/css2?family=Arimo:wght@400;700&display=swap" rel="stylesheet">
<style>
  :root {
    --page-bg: #ececec;
    --card-dark: #1b1f1e;
    --card-light: #fbfbfa;
    --accent: #ea5a1f;
    --ink: #1e1e1e;
  }
  html, body {
    margin: 0;
    width: 1200px;
    height: 864px;
    overflow: hidden;
    background: var(--page-bg);
    font-family: "Arimo", Arial, sans-serif;
  }
  .business-card {
    position: absolute;
    left: 75px;
    top: 132px;
    width: 1050px;
    height: 600px;
    background: var(--card-dark);
    overflow: hidden;
    box-shadow: 0 10px 30px rgba(0,0,0,0.18);
  }
  .card-shapes {
    position: absolute;
    inset: 0;
  }
  .brand {
    position: absolute;
    left: 560px;
    top: 70px;
    width: 440px;
    height: 150px;
    display: flex;
    align-items: center;
    justify-content: center;
    gap: 20px;
  }
  .brand-dot {
    width: 64px;
    height: 64px;
    border-radius: 50%;
    background: var(--accent);
    flex: none;
  }
  .brand-name {
    font-weight: 700;
    font-size: 68px;
    color: var(--ink);
    letter-spacing: 1px;
  }
  .contact-list {
    position: absolute;
    left: 560px;
    top: 262px;
    margin: 0;
    padding: 0;
    list-style: none;
  }
  .contact-item {
    display: flex;
    align-items: center;
    gap: 22px;
    height: 50px;
    font-size: 25px;
    color: var(--ink);
    white-space: nowrap;
  }
  .contact-item:nth-child(2) { margin-left: 6px; }
  .contact-item:nth-child(3) { margin-left: 12px; }
  .contact-item:nth-child(4) { margin-left: 18px; }
  .contact-icon {
    width: 26px;
    height: 26px;
    flex: none;
    background: var(--accent);
    border-radius: 3px;
    display: flex;
    align-items: center;
    justify-content: center;
  }
  .contact-icon svg { width: 18px; height: 18px; }
  .web-link {
    position: absolute;
    left: 600px;
    top: 478px;
    font-size: 25px;
    color: var(--ink);
    white-space: nowrap;
  }
  .holder-name {
    position: absolute;
    left: 60px;
    bottom: 45px;
    margin: 0;
    font-weight: 400;
    font-size: 48px;
    color: var(--accent);
    white-space: nowrap;
  }
</style>
</head>
<body>
  <div class="business-card">
    <svg class="card-shapes" viewBox="0 0 1050 600" width="1050" height="600" aria-hidden="true">
      <path d="M470 0 C300 130 290 430 540 600 L1050 600 L1050 0 Z" fill="var(--accent)"/>
      <path d="M505 0 C350 140 345 430 585 600 L1050 600 L1050 0 Z" fill="var(--card-light)"/>
    </svg>

    <div class="brand">
      <span class="brand-dot"></span>
      <span class="brand-name">Larkmoor</span>
    </div>

    <ul class="contact-list">
      <li class="contact-item">
        <span class="contact-icon">
          <svg viewBox="0 0 24 24"><path fill="#fff" d="M6.6 10.8a15 15 0 0 0 6.6 6.6l2.2-2.2a1 1 0 0 1 1-.25 11.4 11.4 0 0 0 3.6.57 1 1 0 0 1 1 1V20a1 1 0 0 1-1 1A17 17 0 0 1 3 4a1 1 0 0 1 1-1h3.5a1 1 0 0 1 1 1c0 1.250.2 2.45.57 3.57a1 1 0 0 1-.25 1z"/></svg>
        </span>
        (816) 555-0193
      </li>
      <li class="contact-item">
        <span class="contact-icon">
          <svg viewBox="0 0 24 24"><circle cx="12" cy="12" r="8" fill="none" stroke="#fff" stroke-width="2"/><path d="M4 12h16M12 4c3 3 3 13 0 16M12 4c-3 3-3 13 0 16" fill="none" stroke="#fff" stroke-width="1.6"/></svg>
        </span>
        Larkmoor.com
      </li>
      <li class="contact-item">
        <span class="contact-icon">
          <svg viewBox="0 0 24 24"><rect x="3" y="6" width="18" height="12" fill="none" stroke="#fff" stroke-width="2"/><path d="M3 6l9 7 9-7" fill="none" stroke="#fff" stroke-width="2"/></svg>
        </span>
        peterholloway@larkmoor.com
      </li>
      <li class="contact-item">
        <span class="contact-icon">
          <svg viewBox="0 0 24 24"><rect x="7" y="7" width="10" height="10" fill="#fff"/></svg>
        </span>
        http://gallery.larkmoor.com
      </li>
    </ul>

    <div class="web-link">larkmoor.com/GroundsandGarden</div>

    <h1 class="holder-name">Peter Holloway</h1>
  </div>
</body>
</html>
```